Fahrzeugbeschriftung für einen Hofladen
Zielgruppe
Biologische Produkte an den Endverbraucher vermarkten. Vorallem Kartoffel, Eier und Getreide.
24 h Hofladen
Aufgabenstellung
ansprechendes Design mit unseren Logo
Es soll das vorhandene Logo + Telfonnummer,Ort und Homepage oben stehn.
KL Lastwiesel R8 Kastenwagen (In Fahrtrichtung links Befindet sich auf der Seite ein Lufthutze)

```html
<!DOCTYPE html>
<html lang="de">
<head>
<meta charset="utf-8">
<title>Fahrzeugbeschriftung Biohof Lindner</title>
<link rel="stylesheet" href="https://fonts.googleapis.com/css2?family=Open+Sans:wght@400;600;700&display=swap">
<style>
  :root {
    --wrap-white: #f6f6f4;
    --wrap-dark: #3a3a3a;
    --accent-green: #b2c23a;
    --text-grey: #5b5554;
    --logo-white: #ffffff;
    --page: #ffffff;
  }
  html, body {
    margin: 0;
    width: 1200px;
    height: 728px;
    overflow: hidden;
    background: var(--page);
    font-family: "Open Sans", Arial, sans-serif;
  }
  .wrap-panel {
    position: absolute;
    left: 40px;
    top: 120px;
    width: 1120px;
    height: 420px;
    border-radius: 28px;
    overflow: hidden;
    background: var(--wrap-white);
  }
  .wrap-shapes {
    position: absolute;
    inset: 0;
  }
  .contact-block {
    position: absolute;
    left: 270px;
    top: 200px;
    color: var(--text-grey);
  }
  .contact-phone {
    font-weight: 700;
    font-size: 31px;
    letter-spacing: 0.5px;
    margin: 0 0 6px;
  }
  .contact-address {
    margin: 0 0 0 36px;
    font-size: 15px;
    line-height: 20px;
    font-style: normal;
  }
  .brand-name {
    position: absolute;
    left: 800px;
    top: 100px;
    margin: 0;
    color: var(--logo-white);
    font-weight: 600;
    font-size: 46px;
    line-height: 52px;
  }
  .website {
    position: absolute;
    left: 812px;
    top: 230px;
    color: var(--accent-green);
    font-size: 20px;
    font-weight: 400;
  }
</style>
</head>
<body>
  <main class="wrap-panel">
    <svg class="wrap-shapes" width="1120" height="420" viewBox="0 0 1120 420">
      <path class="dark-field" d="M610 0 H1120 V420 H560 C600 330 560 250 600 170 C630 110 600 50 610 0 Z" fill="var(--wrap-dark)"/>
      <path class="green-swoosh" d="M800 290 C900 265 1020 255 1120 262 V282 C1020 276 900 280 800 290 Z" fill="var(--accent-green)"/>
    </svg>

    <section class="contact-block">
      <p class="contact-phone">02274/58162</p>
      <address class="contact-address">
        Biohof Lindner<br>
        Mühlweg 7<br>
        3442 Wiesenfeld
      </address>
    </section>

    <h1 class="brand-name">Biohof<br>Lindner</h1>
    <div class="website">www.biohoflindner.at</div>
  </main>
</body>
</html>
```